Business card to promote business guidance

I need a card design to give to all my customers advertising a way to build a business exactly like the one they just bought from. I have an online store and will include one with each shipment. It should state the way to financial freedom and working for yourself

Target Market(s)

Young Entrepreneurs that want to start and don't know how

Industry/Entity Type

Business

Contact Information for Business Card

"You just bought from a successful company on Brindlemart. I have a unique business model, discovered by me, unlike any other that can make anyone successful. Follow me and message me for exactly the same model. If you ever wanted to work for yourself, I will teach you how. It's not a pipe dream, allow me to guide you out of the box."

Colors
85abd2

Requirements
Must have
• website www.dorianwelkby.example
snapgrove @thedorianwelkby

```html
<!DOCTYPE html>
<html lang="en">
<head>
<meta charset="utf-8">
<title>Dorian Welkby – Business Card</title>
<link href="https://fonts.googleapis.com/css2?family=Carlito:wght@700&family=Arvo:wght@700&display=swap" rel="stylesheet">
<style>
  :root {
    --page-bg: #ececec;
    --card-teal-light: #2fb4c6;
    --card-teal-mid: #1a9db0;
    --card-teal-deep: #127f92;
    --panel-fill: rgba(8, 48, 62, 0.72);
    --message-text: #ffffff;
    --contact-text: #0f2c3a;
  }
  html, body {
    margin: 0;
    padding: 0;
    width: 1200px;
    height: 900px;
    overflow: hidden;
    background: var(--page-bg);
  }
  .business-card {
    position: absolute;
    left: 100px;
    top: 140px;
    width: 1000px;
    height: 620px;
    overflow: hidden;
    box-shadow: 0 10px 30px rgba(0, 0, 0, 0.18);
  }
  .card-backdrop {
    position: absolute;
    inset: 0;
    background:
      radial-gradient(ellipse at 30% 35%, var(--card-teal-mid) 0%, transparent 60%),
      radial-gradient(ellipse at 60% 90%, var(--card-teal-light) 0%, transparent 65%),
      linear-gradient(180deg, var(--card-teal-deep) 0%, var(--card-teal-mid) 45%, var(--card-teal-light) 100%);
  }
  .message-panel {
    position: absolute;
    inset: 0;
    width: 1000px;
    height: 620px;
  }
  .card-message {
    position: absolute;
    left: 100px;
    top: 118px;
    width: 800px;
    margin: 0;
    font-family: "Carlito", "Calibri", sans-serif;
    font-weight: 700;
    font-size: 32px;
    line-height: 45px;
    color: var(--message-text);
    text-align: center;
  }
  .card-contact {
    position: absolute;
    left: 0;
    top: 500px;
    width: 1000px;
    margin: 0;
    font-family: "Arvo", serif;
    font-weight: 700;
    font-size: 33px;
    line-height: 45px;
    color: var(--contact-text);
    text-align: center;
  }
  .card-contact span { display: block; }
</style>
</head>
<body>
  <div class="business-card">
    <div class="card-backdrop" role="img" aria-label="Blurred teal photograph with falling multicoloured confetti"></div>
    <svg class="message-panel" viewBox="0 0 1000 620" aria-hidden="true">
      <path d="M18,18 Q500,100 982,18 Q900,264 982,510 Q500,430 18,510 Q100,264 18,18 Z" fill="var(--panel-fill)"/>
    </svg>
    <p class="card-message">
      You just bought from a successful company on<br>
      Brindlemart. I have a unique business model,<br>
      discovered by me, unlike any other that can make<br>
      anyone successful.&nbsp; Follow me and message me<br>
      for exactly the same model. If you ever wanted to<br>
      work for yourself, I will teach you how.&nbsp; It's not a<br>
      pipe dream, allow me to guide you out of the box
    </p>
    <p class="card-contact">
      <span class="contact-website">www.dorianwelkby.example</span>
      <span class="contact-social">snapgrove @thedorianwelkby</span>
    </p>
  </div>
</body>
</html>
```